Tiny Petal Product Label for Tear-Free Head-to-Toe Wash

Need a bottle label design for a new line of natural products targeting infants and children. Products are Pediatrician-developed and paraben-free, sulfate-free, fragrance-free, and cruelty-free. Design should be clean and have a high-end feel to it. Will need other product labels in Tiny Petal line designed as well in upcoming projects.

Target Market(s)

Newborn to young elementary age children and their parents

Industry/Entity Type

Cosmetics/Beauty

Font styles to use
Other font styles liked:
• Brand fonts are Jost and Sonorous

Colors

Designer to choose colors to be used in the design.

Requirements
Must have
• Tiny Petal logo, Pediatrician Developed logo, and a clean high-end feel to it. The label must fit the specialty bottle we will be using (label measurements and diagram will be provided) for the front and back of bottle only (NOT the side labels). It must include our list of ingredients (will provide once designer selected).
Nice to have
• Should stand out on the shelf of other baby products due to it's clean simplicity and high-end feel
Should not have
• too much of a "kiddie" feel to it (targeting the parents not the kids)

```html
<!DOCTYPE html>
<html lang="en">
<head>
<meta charset="UTF-8">
<title>Tiny Petal Back Label</title>
<link href="https://fonts.googleapis.com/css2?family=Jost:wght@400;500&display=swap" rel="stylesheet">
<style>
  :root {
    --page: #ffffff;
    --label: #f6f0ea;
    --heading: #7d8a84;
    --ink: #3c3c3c;
    --badge: #4a4a4c;
  }
  html, body {
    margin: 0;
    width: 1200px;
    height: 1200px;
    overflow: hidden;
    background: var(--page);
    font-family: "Jost", sans-serif;
  }
  .back-label {
    position: absolute;
    left: 257px;
    top: 136px;
    width: 686px;
    height: 928px;
    background: var(--label);
    border-radius: 64px 64px 26px 26px;
    color: var(--ink);
    text-align: center;
  }
  .section-title {
    position: absolute;
    left: 0;
    right: 0;
    top: 44px;
    margin: 0;
    font-size: 50px;
    font-weight: 400;
    letter-spacing: 2px;
    color: var(--heading);
  }
  .ingredient-list {
    position: absolute;
    left: 140px;
    right: 140px;
    top: 132px;
    margin: 0;
    font-size: 24px;
    line-height: 31px;
    letter-spacing: 0.3px;
  }
  .directions-title {
    position: absolute;
    left: 0;
    right: 0;
    top: 494px;
    margin: 0;
    font-size: 24px;
    font-weight: 400;
    letter-spacing: 0.5px;
  }
  .directions-text {
    position: absolute;
    left: 0;
    right: 0;
    top: 548px;
    margin: 0;
    font-size: 24px;
    line-height: 32px;
    letter-spacing: 0.3px;
  }
  .approval-badge {
    position: absolute;
    left: 259px;
    top: 647px;
    width: 168px;
    height: 168px;
  }
  .claims {
    position: absolute;
    left: 0;
    right: 0;
    top: 870px;
    font-size: 19px;
    letter-spacing: 0.3px;
  }
  .claim {
    position: absolute;
    top: 0;
    transform: translateX(-50%);
    white-space: nowrap;
  }
  .claim--left { left: 222px; }
  .claim--right { left: 494px; }
</style>
</head>
<body>
  <section class="back-label">
    <h2 class="section-title">INGREDIENTS</h2>
    <p class="ingredient-list">Water, Glycerin, Cocos Nucrifera (Coconut) Oil, Cetearyl Alcohal, Ai-loe Barbadensis Leaf Juice, Eutyros-permum Parkl. (Shea) Butter, Glyce-tyl Stearate.-Caprylla/Capric Tri-glyceride, Simmondsia, Chinensis (Jojoba) Sead Oil, Sudlum Stearoyl Lactylate, Tocopherol, Xanthan Gum, Citric</p>
    <h3 class="directions-title">DIRECTIONS</h3>
    <p class="directions-text">Apply as needed to baby’s skin.<br>For external use only.</p>
    <svg class="approval-badge" viewBox="0 0 168 168" role="img" aria-label="Pediatrician developed badge">
      <circle cx="84" cy="84" r="78" fill="none" stroke="var(--badge)" stroke-width="4"/>
      <circle cx="84" cy="84" r="40" fill="var(--badge)"/>
    </svg>
    <div class="claims">
      <span class="claim claim--left">FRAGRANCE-FREE</span>
      <span class="claim claim--right">MADE IN JAPAN</span>
    </div>
  </section>
</body>
</html>
```